Update our OBGYN business card look and info

We are an OBGYN office. Our logo is nice but would like to "woman" part of the logo to be a darker color, to contrast with the flower that surrounds it. Maybe make our practice name Bloom Circle Health more feminine. Our practice caters to women only. All providers and staff are female.

Target Market(s)

Females 16-65.

Industry/Entity Type

Business

Contact Information for Business Card

See attached upload. The ONLY CHANGE to the information is DELETE the name Marla Quenbright, Midwife and REPLACE with Tessa Dravinoux, Midwife

Logo Text

Bloom Circle Health Obstetrics & Gynecology

Font styles to use
Serif
Script

Colors
85cae6
0692cd
33a6d7
85abd2
f59195
eea4c8
cadf82
fac994
d3a5cc

```html
<!DOCTYPE html>
<html lang="en">
<head>
<meta charset="utf-8">
<title>Bloom Circle Health – Business Cards</title>
<link href="https://fonts.googleapis.com/css2?family=Cormorant+Garamond:wght@600&family=Open+Sans:wght@400;600&display=swap" rel="stylesheet">
<style>
  :root{
    --backdrop:#6e6e6e;
    --card-blue:#7fbccb;
    --card-white:#f7f7f7;
    --brand-maroon:#6b2a2e;
    --brand-teal:#5aaec4;
    --text-grey:#6a6a6a;
    --mark-faint:#e4e4e4;
    --white:#ffffff;
  }
  *{margin:0;padding:0;box-sizing:border-box}
  html,body{width:1200px;height:904px;overflow:hidden}
  body{background:var(--backdrop);font-family:"Open Sans",sans-serif;position:relative}

  .card{position:absolute;border-radius:3px;box-shadow:0 10px 24px rgba(0,0,0,.35);overflow:hidden}

  /* back side */
  .card--back{left:90px;top:110px;width:540px;height:309px;background:var(--card-blue)}
  .back-brand{position:absolute;left:0;right:0;top:112px;display:flex;align-items:center;justify-content:center;gap:14px;
    color:var(--white);font-family:"Cormorant Garamond",serif;font-size:36px;font-weight:600}
  .back-brand .dot{width:22px;height:22px;border-radius:50%;background:var(--white)}
  .back-url{position:absolute;left:0;right:0;bottom:34px;text-align:center;color:var(--white);font-size:14px;letter-spacing:4px}

  /* front side */
  .card--front{left:480px;top:430px;width:640px;height:366px;background:var(--card-white)}
  .front-brand{position:absolute;left:42px;top:44px;display:flex;align-items:center;gap:14px}
  .front-brand .dot{width:44px;height:44px;border-radius:50%;background:var(--brand-teal)}
  .front-brand .name{font-family:"Cormorant Garamond",serif;font-weight:600;font-size:34px;line-height:1;color:var(--brand-maroon)}
  .front-brand .specialty{font-size:14px;font-weight:600;line-height:1.4;color:var(--brand-maroon);margin-top:2px}
  .faint-mark{position:absolute;left:300px;top:178px;width:170px;height:170px;border-radius:50%;background:var(--mark-faint)}

  .providers{position:absolute;right:42px;top:66px;text-align:right;color:var(--text-grey);font-size:16px;line-height:1.55;list-style:none}

  .contact{position:absolute;left:42px;bottom:40px;color:var(--text-grey);font-size:15px;line-height:1.5;list-style:none}
  .contact li{display:flex;align-items:flex-start;gap:10px}
  .contact svg{width:14px;height:14px;margin-top:4px;flex:none;fill:var(--brand-teal)}
  .contact .indent{padding-left:24px}
</style>
</head>
<body>

<section class="card card--back">
  <div class="back-brand"><span class="dot"></span>Bloom Circle Health</div>
  <p class="back-url">www.bloomcirclehealth.com</p>
</section>

<section class="card card--front">
  <div class="faint-mark"></div>

  <div class="front-brand">
    <span class="dot"></span>
    <div>
      <div class="name">Bloom Circle Health</div>
      <div class="specialty">Obstetrics &amp; Gynecology</div>
    </div>
  </div>

  <ul class="providers">
    <li>Renata Solvik, MD</li>
    <li>Danica Merrow, MD</li>
    <li>Lisette Farwin, MD</li>
    <li>Tessa Dravinoux, Midwife</li>
    <li>Odelia Brancott, Midwife</li>
  </ul>

  <ul class="contact">
    <li><svg viewBox="0 0 24 24"><path d="M12 2a7 7 0 0 0-7 7c0 5 7 13 7 13s7-8 7-13a7 7 0 0 0-7-7zm0 9.5A2.5 2.5 0 1 1 12 6.5a2.5 2.5 0 0 1 0 5z"/></svg>418 Larkspur Ave, Ste 3B</li>
    <li class="indent">Fernvale, GA 30999-1204</li>
    <li><svg viewBox="0 0 24 24"><path d="M6.6 10.8a15 15 0 0 0 6.6 6.6l2.2-2.2a1 1 0 0 1 1-.25 11.4 11.4 0 0 0 3.6.57 1 1 0 0 1 1 1V20a1 1 0 0 1-1 1A17 17 0 0 1 3 4a1 1 0 0 1 1-1h3.5a1 1 0 0 1 1 1c0 1.25.2 2.45.57 3.57a1 1 0 0 1-.25 1z"/></svg>555-014-2287</li>
    <li><svg viewBox="0 0 24 24"><path d="M6 3h12v5H6zM4 9h16a2 2 0 0 1 2 2v7h-4v3H6v-3H2v-7a2 2 0 0 1 2-2zm4 7v3h8v-3z"/></svg>555-014-2291</li>
    <li><svg viewBox="0 0 24 24"><path d="M12 2a10 10 0 1 0 0 20 10 10 0 0 0 0-20zm6.9 9h-3a15 15 0 0 0-1.3-5.6A8 8 0 0 1 18.9 11zM12 4.1c.9 1.3 1.8 3.7 1.9 6.9h-3.8c.1-3.2 1-5.6 1.9-6.9zM9.4 5.4A15 15 0 0 0 8.1 11h-3a8 8 0 0 1 4.3-5.6zM5.1 13h3a15 15 0 0 0 1.3 5.6A8 8 0 0 1 5.1 13zm6.9 6.9c-.9-1.3-1.8-3.7-1.9-6.9h3.8c-.1 3.2-1 5.6-1.9 6.9zm2.6-1.3a15 15 0 0 0 1.3-5.6h3a8 8 0 0 1-4.3 5.6z"/></svg>www.bloomcirclehealth.com</li>
  </ul>
</section>

</body>
</html>
```